Digital Marketing Agency Business Card Design Project

We are a boutique marketing agency that provides premium digital marketing services that invlude
- strategic marketing plans
- Plovex Clickreach advertising
- Search engine optimization
- Digital business analytics
- Digital merketing consulting
Business card must have a premium look that makes c clear statement. We provide digital marketing services for multiple languages.

Business card on the back side should have a slogan. Boutique digital marketing.

We always go the extra mile by every project so that clients gep premium solution and 100% satisfaction.

Please design a business card that is one of a kind..

Thank you.

Psd logo uploaded and brief updated.

Target Market(s)

Companies that need strategic online presence that is reached with boutique digital marketing services in all verticals.

Industry/Entity Type

Marketing

Font styles to use
Sans Serif

Requirements
Must have
• Premium and prestigious look.
Nice to have
• Design unique business card that fits with provided logo.
Logo should include:
Tel., E-mail, web address
Business title: one is CEO, second is COO.
Business address.

Try designing dark and light version, dark with the grey-silver from the logo and light just white background with some abstract curves in blue or green.
Should not have
• No old-style design and font
No need to list our services on the business card.

```html
<!DOCTYPE html>
<html lang="en">
<head>
<meta charset="utf-8">
<title>Velsora – Business Card</title>
<link rel="stylesheet" href="https://fonts.googleapis.com/css2?family=Jost:wght@400;600&display=swap">
<style>
  :root {
    --coral: #ff625f;
    --ink: #3f4356;
    --paper: #ffffff;
    --edge: #a9abb3;
  }
  html, body {
    margin: 0;
    width: 1200px;
    height: 1000px;
    overflow: hidden;
    background: var(--paper);
    font-family: "Jost", sans-serif;
  }
  .card {
    position: absolute;
    left: 77px;
    top: 200px;
    width: 1047px;
    height: 598px;
    border: 1px solid var(--edge);
    background: var(--paper);
  }
  .brand-band {
    position: absolute;
    left: 0;
    top: 0;
    width: 235px;
    height: 100%;
    background: var(--coral);
  }
  .brand-name {
    position: absolute;
    left: 45px;
    top: 50px;
    height: 470px;
    writing-mode: vertical-rl;
    transform: rotate(180deg);
    margin: 0;
    font-size: 82px;
    font-weight: 600;
    line-height: 82px;
    letter-spacing: 12px;
    color: var(--ink);
    text-align: center;
  }
  .brand-tagline {
    position: absolute;
    left: 146px;
    top: 48px;
    height: 500px;
    writing-mode: vertical-rl;
    transform: rotate(180deg);
    margin: 0;
    font-size: 23px;
    font-weight: 400;
    line-height: 28px;
    letter-spacing: 3.2px;
    color: var(--paper);
    text-align: center;
  }
  .contact-panel {
    position: absolute;
    left: 248px;
    top: 0;
    right: 0;
    height: 324px;
    background: var(--coral);
    color: var(--paper);
    text-align: right;
  }
  .contact-panel .person {
    position: absolute;
    right: 61px;
    top: 44px;
    margin: 0;
    font-size: 38px;
    font-weight: 400;
    letter-spacing: 1px;
    line-height: 1;
  }
  .contact-panel .details {
    position: absolute;
    right: 61px;
    top: 98px;
    margin: 0;
    font-style: normal;
    line-height: 1;
  }
  .details .phone {
    display: block;
    font-size: 32px;
    letter-spacing: 2px;
  }
  .details .email {
    display: block;
    margin-top: 10px;
    font-size: 29px;
    letter-spacing: 0.5px;
  }
  .services {
    position: absolute;
    right: 59px;
    top: 375px;
    margin: 0;
    padding: 0;
    list-style: none;
    text-align: right;
    color: var(--ink);
    font-size: 34px;
    line-height: 45px;
    letter-spacing: 1.6px;
    word-spacing: 5px;
  }
  .services li::after {
    content: " -";
  }
</style>
</head>
<body>
  <article class="card">
    <section class="brand-band">
      <p class="brand-name">VELSORA</p>
      <p class="brand-tagline">BOUTIQUE DIGITAL MARKETING</p>
    </section>
    <section class="contact-panel">
      <h1 class="person">Mira Tolland</h1>
      <address class="details">
        <span class="phone">+ 00 0000 0000</span>
        <span class="email">mira@velsora.com</span>
      </address>
    </section>
    <ul class="services">
      <li>Strategic Marketing Plans</li>
      <li>Plovex Clickreach Advertising</li>
      <li>Search Engine Optimization</li>
      <li>Digital Business Analytics</li>
    </ul>
  </article>
</body>
</html>
```